Lantern Advisory Business Cards

We need a new layout for our business cards. We have a logo already. But we might be interested in only using the Lantern portion of the logo. It has been uploaded.

We would like cards that are not overly busy. Clean. Modern. Perhaps a gray color for one side.

On the back, we would like to have the lantern part of the logo and "Take the Leap, we've got you!"

Our business provides medics and safety training for corporate clients. Our website is www.lanternadvisoryllc.example.

Industry/Entity Type

Business

Contact Information for Business Card

We want include name, email address, cell phone, main line number, and website URL on the front. Use the following as an example: Marla Tobin, marla@lanternadvisoryllc.example, 402.318.7264 (cell), 402.947.315, and www.lanternadvisoryllc.example.

Font styles to use
Serif
Sans Serif

Requirements
Must have
• All required information. Back side logo with "Step forward, we stand ready!"
Nice to have
• If possible, we would like to consider creating a card in a non-standard shape. Perhaps, the shape of a lantern. Just interested in understanding the option.

```html
<!DOCTYPE html>
<html lang="en">
<head>
<meta charset="utf-8">
<title>Lantern Advisory Business Cards</title>
<link rel="stylesheet" href="https://fonts.googleapis.com/css2?family=Arimo:wght@400;700&display=swap">
<style>
  :root {
    --backdrop: #d8d3cb;
    --label-blue: #1f5aa6;
    --label-dark: #111111;
    --card-navy: #1f3d70;
    --card-navy-edge: #2c4f8a;
    --card-frost: #eef2f6;
    --card-frost-edge: #8ea3bd;
    --ink-light: #e6ecf5;
    --ink-navy: #1c2f55;
    --ink-gray: #3c4658;
  }
  html, body {
    margin: 0;
    padding: 0;
    width: 1200px;
    height: 970px;
    overflow: hidden;
    background: var(--backdrop);
  }
  .canvas {
    position: relative;
    width: 1200px;
    height: 970px;
    font-family: "Arimo", Arial, sans-serif;
  }
  .label {
    position: absolute;
    margin: 0;
    font-weight: 400;
    line-height: 1;
  }
  .label--title { left: 118px; top: 36px; font-size: 48px; color: var(--label-blue); }
  .label--back  { left: 990px; top: 490px; font-size: 44px; color: var(--label-blue); }
  .label--front { left: 42px;  top: 740px; font-size: 44px; color: var(--label-dark); }
  .card {
    position: absolute;
    width: 512px;
    height: 444px;
    overflow: visible;
  }
  .card--back  { left: 564px; top: 188px; }
  .card--front { left: 136px; top: 432px; }
  .card-shape--front { fill: var(--card-navy); stroke: var(--card-navy-edge); stroke-width: 2; opacity: 0.94; }
  .card-shape--back  { fill: var(--card-frost); stroke: var(--card-frost-edge); stroke-width: 2; opacity: 0.92; }
  .card-inner-line { fill: none; stroke: var(--ink-navy); stroke-width: 1.2; opacity: 0.6; }
  .holder-name { font-weight: 700; font-size: 29px; fill: var(--ink-light); }
  .contact { font-size: 18px; fill: var(--ink-light); }
  .icon-line { fill: none; stroke: var(--ink-light); stroke-width: 1.8; }
  .icon-fill { fill: var(--ink-light); }
  .brand-name { font-weight: 400; font-size: 22px; fill: var(--ink-navy); }
  .brand-tagline { font-size: 11px; fill: var(--ink-gray); }
  .brand-mark { fill: none; stroke: var(--ink-navy); stroke-width: 1.5; }
  .slogan { font-size: 17px; fill: var(--ink-navy); }
  .website { font-size: 16px; fill: var(--ink-gray); }
</style>
</head>
<body>
<main class="canvas">
  <h1 class="label label--title">Transparent Card</h1>

  <svg class="card card--back" viewBox="0 0 512 444" aria-label="Back side of the card">
    <path class="card-shape--back" d="M0,150 Q256,-100 512,150 L512,205 L256,444 L0,205 Z"/>
    <path class="card-inner-line" d="M18,158 Q256,-72 494,158 L494,208 L256,426 L18,208 Z"/>
    <circle class="brand-mark" cx="256" cy="78" r="10"/>
    <text class="brand-name" x="256" y="122" text-anchor="middle">Lantern Advisory</text>
    <text class="brand-tagline" x="256" y="141" text-anchor="middle">Ready When It Matters</text>
    <text class="slogan" x="256" y="178" text-anchor="middle">Step forward, we stand ready!</text>
    <text class="website" x="256" y="248" text-anchor="middle">www.lanternadvisoryllc.example</text>
  </svg>

  <p class="label label--back">Back Side</p>

  <svg class="card card--front" viewBox="0 0 512 444" aria-label="Front side of the card">
    <path class="card-shape--front" d="M0,150 Q256,-100 512,150 L512,205 L256,444 L0,205 Z"/>
    <text class="holder-name" x="256" y="70" text-anchor="middle">Marla Tobin</text>

    <rect class="icon-line" x="101" y="103" width="11" height="19" rx="2"/>
    <text class="contact" x="124" y="120">402.318.7264</text>

    <path class="icon-fill" d="M268,108 q10,-6 20,0 l-2,4 h-3 l-1,-2 q-4,-1 -8,0 l-1,2 h-3 z M270,113 h16 v8 h-16 z"/>
    <text class="contact" x="294" y="120">402.947.315</text>

    <rect class="icon-line" x="95" y="143" width="17" height="12"/>
    <path class="icon-line" d="M95,143 L103.5,150 L112,143"/>
    <text class="contact" x="124" y="155">marla@lanternadvisoryllc.example</text>
  </svg>

  <p class="label label--front">Front Side</p>
</main>
</body>
</html>
```